BY GRIT WE ROLL

Label design for a variety of BBQ sauces, cooking sauces, and marinades. This will be the template for sauces sourced from Telluride, Colorado. Telluride is now know as a world-class ski resort, but historically was a gold and silver mining area. "By Grit We Roll" was what the train conductors used to call out as trains entered Telluride in the late 1800s as Telluride was notorious for being a semi-lawless town of 2,000. There used to be a lot of bars, prostitutes, etc. Telluride was also the location of Rufus Penwarden's first bank robbery. Label design must reflect an old timey western feel.

Cooking

```html
<!DOCTYPE html>
<html lang="en">
<head>
<meta charset="utf-8">
<title>By Grit We Roll — BBQ Sauce Label</title>
<link rel="stylesheet" href="https://fonts.googleapis.com/css2?family=Rye&family=Alfa+Slab+One&display=swap">
<style>
  :root {
    --page-bg: #f2f3f5;
    --label-paper: #e3b65c;
    --label-paper-light: #ecca7e;
    --label-paper-dark: #c9913f;
    --ink-brown: #5b2914;
    --scene-rust: #b8672f;
    --scene-umber: #8e4a22;
    --scene-sand: #d9a656;
  }
  html, body {
    margin: 0;
    padding: 0;
    width: 964px;
    height: 1200px;
    overflow: hidden;
    background: var(--page-bg);
  }
  .canvas {
    position: relative;
    width: 964px;
    height: 1200px;
  }
  .label {
    position: absolute;
    left: 154px;
    top: 30px;
    width: 656px;
    height: 1140px;
    background:
      radial-gradient(ellipse at 30% 20%, var(--label-paper-light) 0%, transparent 55%),
      radial-gradient(ellipse at 80% 85%, var(--label-paper-dark) 0%, transparent 60%),
      var(--label-paper);
    color: var(--ink-brown);
    text-align: center;
    overflow: hidden;
  }
  .brand-title {
    position: absolute;
    left: 0;
    right: 0;
    top: 110px;
    margin: 0;
    font-family: "Rye", "Alfa Slab One", serif;
    font-weight: 400;
    font-size: 104px;
    line-height: 140px;
    letter-spacing: 2px;
  }
  .rule {
    position: absolute;
    left: 60px;
    right: 60px;
    height: 6px;
    background: var(--ink-brown);
  }
  .rule--title { top: 440px; }
  .rule--product-top { top: 800px; }
  .rule--product-bottom { top: 984px; }
  .scene-art {
    position: absolute;
    left: 0;
    right: 0;
    top: 470px;
    height: 480px;
    background:
      radial-gradient(ellipse at 50% 45%, var(--scene-umber) 0%, var(--scene-rust) 35%, transparent 70%),
      linear-gradient(180deg, transparent 0%, var(--scene-sand) 40%, var(--scene-rust) 100%);
    opacity: 0.75;
  }
  .product-name {
    position: absolute;
    left: 0;
    right: 0;
    top: 826px;
    margin: 0;
    font-family: "Rye", "Alfa Slab One", serif;
    font-weight: 400;
    font-size: 96px;
    line-height: 140px;
    letter-spacing: 2px;
  }
  .net-weight {
    position: absolute;
    left: 0;
    right: 0;
    top: 1030px;
    margin: 0;
    font-family: "Rye", "Alfa Slab One", serif;
    font-size: 26px;
    letter-spacing: 1px;
  }
</style>
</head>
<body>
  <main class="canvas">
    <section class="label">
      <div class="scene-art" role="img" aria-label="Faded western illustration of a horse rider and a train with a flame emblem in rust tones"></div>
      <h1 class="brand-title">BY GRIT<br>WE ROLL</h1>
      <div class="rule rule--title"></div>
      <div class="rule rule--product-top"></div>
      <h2 class="product-name">BBQ SAUCE</h2>
      <div class="rule rule--product-bottom"></div>
      <p class="net-weight">NET WT 12 FL OZ</p>
    </section>
  </main>
</body>
</html>
```